Banner Ads for Lumorank.biz

Hello everyone! We are a online advertising company, and we offer a few unique solutions for advertiser and publishers.
we also buy and sell website traffic!
and for this service we would like to produce some ad banners to promote our offers.
we would like to create the banner in the following formats:
Fullsize Banner 468 x 60
Halfsize Banner 234 x 60
Square Banner 125 x 125
Skyscraper 120 x 600
Bold Skyscraper 160 x 600
Medium Rectangle 300 x 250
Vertical Rectangle 240 x 400
Pop-Up 250 x 250
Industry/Entity Type
Advertising
Requirements
Must have
- catchy design - modern, cool. Maybe Cartoon style
Our LumoRank.biz Logo (only the mascot)
Banners must be animated!

```html
<!DOCTYPE html>
<html lang="en">
<head>
<meta charset="utf-8">
<title>LumoRank.biz Skyscraper Banners</title>
<link rel="stylesheet" href="https://fonts.googleapis.com/css2?family=Arimo:wght@400;700&display=swap">
<style>
  :root {
    --page-bg: #ffffff;
    --frame: #9a9a9a;
    --brand-red: #c8120f;
    --ribbon-top: #c9140f;
    --ribbon-bottom: #9a0806;
    --ribbon-fold: #6e0404;
    --tab-black: #141414;
    --ink: #111111;
    --muted: #666666;
    --arc-blue: #1c5ead;
    --button-top: #ff3a34;
    --button-bottom: #c40000;
    --button-disc: #5a0000;
    --white: #ffffff;
  }
  html, body {
    margin: 0;
    width: 900px;
    height: 1200px;
    overflow: hidden;
    background: var(--page-bg);
  }
  .canvas {
    position: relative;
    width: 900px;
    height: 1200px;
  }
  .skyscraper {
    position: absolute;
    top: 164px;
    width: 240px;
    height: 900px;
  }
  .skyscraper--monetize { left: 210px; }
  .skyscraper--buzz { left: 464px; }
  .skyscraper svg { display: block; }
  .brand-name {
    font-family: "Arimo", Arial, sans-serif;
    font-weight: 700;
    fill: var(--brand-red);
  }
  .brand-tagline {
    font-family: "Arimo", Arial, sans-serif;
    font-weight: 400;
    fill: var(--muted);
  }
  .headline {
    font-family: "Arimo", Arial, sans-serif;
    font-weight: 700;
    fill: var(--white);
  }
  .offer {
    font-family: "Arimo", Arial, sans-serif;
    font-weight: 700;
    fill: var(--ink);
  }
  .cta-label {
    font-family: "Arimo", Arial, sans-serif;
    font-weight: 700;
    fill: var(--white);
  }
</style>
</head>
<body>
<main class="canvas">

  <section class="skyscraper skyscraper--monetize" aria-label="Monetize your site banner">
    <svg width="240" height="900" viewBox="0 0 160 600">
      <defs>
        <linearGradient id="stageShade" x1="0" y1="0" x2="0" y2="1">
          <stop offset="0" stop-color="#e6e6e6"/>
          <stop offset="0.45" stop-color="#7a7a7a"/>
          <stop offset="1" stop-color="#000000"/>
        </linearGradient>
        <linearGradient id="ribbonFill" x1="0" y1="0" x2="0" y2="1">
          <stop offset="0" stop-color="var(--ribbon-top)"/>
          <stop offset="1" stop-color="var(--ribbon-bottom)"/>
        </linearGradient>
        <linearGradient id="buttonFill" x1="0" y1="0" x2="0" y2="1">
          <stop offset="0" stop-color="var(--button-top)"/>
          <stop offset="1" stop-color="var(--button-bottom)"/>
        </linearGradient>
        <linearGradient id="photoTone" x1="0" y1="0" x2="0" y2="1">
          <stop offset="0" stop-color="#f4ece6"/>
          <stop offset="0.5" stop-color="#d9a89a"/>
          <stop offset="1" stop-color="#b8c7a6"/>
        </linearGradient>
      </defs>
      <rect class="background" x="0" y="0" width="160" height="600" fill="var(--white)"/>

      <g class="brand">
        <circle cx="30" cy="46" r="10" fill="var(--brand-red)"/>
        <text class="brand-name" x="44" y="53" font-size="19">LumoRank</text>
        <text class="brand-tagline" x="60" y="64" font-size="4">Grow And Rank Your Website Audience</text>
      </g>

      <path class="stage" d="M0 96 Q80 84 160 96 V470 H0 Z" fill="url(#stageShade)"/>
      <rect class="photo-well" x="15" y="270" width="130" height="200" fill="var(--white)"/>
      <rect role="img" aria-label="Photo of a smiling woman holding a fan of dollar bills" x="20" y="288" width="120" height="174" fill="url(#photoTone)"/>

      <rect class="ribbon-tab" x="15" y="100" width="130" height="26" rx="3" fill="var(--tab-black)"/>
      <path class="ribbon-fold" d="M8 112 H152 V272 H8 Z" fill="var(--ribbon-fold)"/>
      <path class="ribbon" d="M12 112 H148 V264 Q80 310 12 264 Z" fill="url(#ribbonFill)"/>
      <g class="headline" text-anchor="middle" font-size="24">
        <text x="80" y="166">Monetize</text>
        <text x="80" y="199">Your</text>
        <text x="80" y="232">Site</text>
        <text x="80" y="265">Now!</text>
      </g>

      <path class="footer-panel" d="M0 468 Q80 440 160 468 V600 H0 Z" fill="var(--white)"/>
      <path class="footer-arc" d="M0 468 Q80 440 160 468" fill="none" stroke="var(--arc-blue)" stroke-width="5"/>

      <g class="offer" text-anchor="middle" font-size="19">
        <text x="80" y="490">BUY &amp; SELL</text>
        <text x="80" y="515">WEBSITE</text>
        <text x="72" y="540">TRAFFIC</text>
      </g>

      <g class="cta">
        <rect x="12" y="552" width="136" height="40" rx="5" fill="url(#buttonFill)"/>
        <text class="cta-label" x="19" y="577" font-size="13">CLICK HERE</text>
        <circle cx="128" cy="572" r="15" fill="var(--button-disc)"/>
        <path d="M124 564 L132 572 L124 580" fill="none" stroke="var(--white)" stroke-width="3" stroke-linecap="round" stroke-linejoin="round"/>
      </g>

      <rect class="frame" x="0.5" y="0.5" width="159" height="599" fill="none" stroke="var(--frame)"/>
    </svg>
  </section>

  <section class="skyscraper skyscraper--buzz" aria-label="Buzz your site traffic banner">
    <svg width="240" height="900" viewBox="0 0 160 600">
      <defs>
        <linearGradient id="stageShade2" x1="0" y1="0" x2="0" y2="1">
          <stop offset="0" stop-color="#e6e6e6"/>
          <stop offset="0.45" stop-color="#7a7a7a"/>
          <stop offset="1" stop-color="#000000"/>
        </linearGradient>
        <linearGradient id="ribbonFill2" x1="0" y1="0" x2="0" y2="1">
          <stop offset="0" stop-color="var(--ribbon-top)"/>
          <stop offset="1" stop-color="var(--ribbon-bottom)"/>
        </linearGradient>
        <linearGradient id="buttonFill2" x1="0" y1="0" x2="0" y2="1">
          <stop offset="0" stop-color="var(--button-top)"/>
          <stop offset="1" stop-color="var(--button-bottom)"/>
        </linearGradient>
        <linearGradient id="illustrationTone" x1="0" y1="0" x2="1" y2="1">
          <stop offset="0" stop-color="#f2f2f2"/>
          <stop offset="0.6" stop-color="#d6dde3"/>
          <stop offset="1" stop-color="#a9c4d6"/>
        </linearGradient>
      </defs>
      <rect class="background" x="0" y="0" width="160" height="600" fill="var(--white)"/>

      <g class="brand">
        <circle cx="30" cy="46" r="10" fill="var(--brand-red)"/>
        <text class="brand-name" x="44" y="53" font-size="19">LumoRank</text>
        <text class="brand-tagline" x="60" y="64" font-size="4">Grow And Rank Your Website Audience</text>
      </g>

      <path class="stage" d="M0 96 Q80 84 160 96 V470 H0 Z" fill="url(#stageShade2)"/>
      <rect class="photo-well" x="15" y="270" width="130" height="200" fill="var(--white)"/>
      <rect role="img" aria-label="Illustration of a cheering figure above a rising green arrow and a target hit by darts" x="20" y="288" width="120" height="174" fill="url(#illustrationTone)"/>

      <rect class="ribbon-tab" x="15" y="100" width="130" height="26" rx="3" fill="var(--tab-black)"/>
      <path class="ribbon-fold" d="M8 112 H152 V272 H8 Z" fill="var(--ribbon-fold)"/>
      <path class="ribbon" d="M12 112 H148 V264 Q80 310 12 264 Z" fill="url(#ribbonFill2)"/>
      <g class="headline" text-anchor="middle" font-size="24">
        <text x="78" y="160">BUZZ</text>
        <text x="78" y="193">Your</text>
        <text x="78" y="226">Site</text>
        <text x="78" y="259">Traffic</text>
      </g>

      <path class="footer-panel" d="M0 468 Q80 440 160 468 V600 H0 Z" fill="var(--white)"/>
      <path class="footer-arc" d="M0 468 Q80 440 160 468" fill="none" stroke="var(--arc-blue)" stroke-width="5"/>

      <g class="offer" text-anchor="middle" font-size="19">
        <text x="80" y="490">BUY &amp; SELL</text>
        <text x="80" y="515">WEBSITE</text>
        <text x="76" y="540">TRAFFIC</text>
      </g>

      <g class="cta">
        <rect x="12" y="552" width="136" height="40" rx="5" fill="url(#buttonFill2)"/>
        <text class="cta-label" x="19" y="577" font-size="13">CLICK HERE</text>
        <circle cx="128" cy="572" r="15" fill="var(--button-disc)"/>
        <path d="M124 564 L132 572 L124 580" fill="none" stroke="var(--white)" stroke-width="3" stroke-linecap="round" stroke-linejoin="round"/>
      </g>

      <rect class="frame" x="0.5" y="0.5" width="159" height="599" fill="none" stroke="var(--frame)"/>
    </svg>
  </section>

</main>
</body>
</html>
```